Business card design needed

OH&S consultancy and training

Industry/Entity Type

Training

Contact Information for Business Card

Coastal Hazard & Skills Collective
Dorian Whitfield
Director

0427 391 608
dorian.whitfield@hzcollect.com.au
hzcollect.com.au

Ph: 03 9172 4309
Fx: 03 9172 4311

```html
<!DOCTYPE html>
<html lang="en">
<head>
<meta charset="utf-8">
<title>Coastal Hazard &amp; Skills Collective – Business Card</title>
<link rel="stylesheet" href="https://fonts.googleapis.com/css2?family=Barlow:wght@400;500&display=swap">
<style>
  :root {
    --navy: #02293b;
    --signal-yellow: #ffe800;
    --mist-grey: #bfc1c3;
    --ink: #1d1d1b;
  }
  html, body {
    margin: 0;
    padding: 0;
    width: 1200px;
    height: 720px;
    overflow: hidden;
    background: var(--navy);
  }
  .card {
    position: relative;
    width: 1200px;
    height: 720px;
    background: var(--navy);
    font-family: "Barlow", sans-serif;
    overflow: hidden;
  }
  .brand {
    position: absolute;
    left: 96px;
    top: 250px;
    display: flex;
    align-items: center;
    gap: 40px;
  }
  .brand-mark {
    width: 150px;
    height: 150px;
    background: var(--signal-yellow);
    flex: none;
  }
  .brand-name {
    margin: 0;
    font-weight: 400;
    font-size: 74px;
    line-height: 1.02;
    letter-spacing: 1px;
    color: var(--mist-grey);
  }
  .web-tab {
    position: absolute;
    left: 0;
    bottom: 0;
    width: 1200px;
    height: 88px;
  }
  .web-tab path {
    fill: var(--signal-yellow);
  }
  .web-address {
    position: absolute;
    left: 0;
    right: 0;
    bottom: 22px;
    margin: 0;
    text-align: center;
    font-size: 35px;
    font-weight: 400;
    letter-spacing: 1.5px;
    color: var(--ink);
    padding-left: 8px;
  }
</style>
</head>
<body>
  <div class="card">
    <div class="brand">
      <div class="brand-mark" aria-hidden="true"></div>
      <h1 class="brand-name">Coastal Hazard &amp;<br>Skills Collective</h1>
    </div>

    <svg class="web-tab" viewBox="0 0 1200 88" aria-hidden="true">
      <path d="M296 88 L336 18 Q346 0 368 0 L826 0 Q848 0 858 18 L892 88 Z"/>
    </svg>
    <p class="web-address">hzcollect.com.au</p>
  </div>
</body>
</html>
```